A golden web-design opportunity

I have created a quick website (www.brintavexgroup.com.au) but I would like to have the website “polished” to look more professional and have a better consistency.

I would like the website to come across as a genuine, professional insight into our business culture but unfortunately my creative skills have reached their limit.

I have attached a media kit PDF so you are better able to establish what are about.
Updates

Hello All! I just wanted to let everyone know that I do not require an ecommerce site! My website is for potential clients to visit, see what we do and get my contact details...

Gathering more feedback

Hello All, I just wanted to let contestants know that there is not a requirement for my team to be mentioned on the website. I cover in person this as part of my presentation with clients. I have uploaded a new Presentation PDF that has this information excluded. Have a good day!

Target Market(s)

Telecommunications professionals; service delivery partners; white collar executives; construction

Industry/Entity Type

Data Communication

Coding

Coded - Design and coding required

Number of Pages Required

3 page

Font styles to use
Other font styles liked:
• Designers discretion

Colors

Designer to choose colors to be used in the design.

Requirements
Must have
• Must be designed so that I can upload it to Plesk, I think that wordpress is preferred.
• - Page:
• - 1 - Full page is a requirement i.e. the website makes full use of the whole screen
• - 2 - Colour scheme must be "muted" and not agressive
• - Links:
• - 1 - All links will work e.g. "E-Mail us" should work
• - 2 - The page identifier ("[LOGO] Home | Brintavex Gruop) will show the Brintavex logo
• - 3 - A link to facebook and linkedin
• - https://www.facebook.com/brintavexgroup
• - https://www.linkedin.com/company/brintavex-group-pty-ltd/
• - 4 - The phone number icon can be clicked on to make a call
• - 5 - The E-Mail icon can be clicked on to send an E-Mail
Nice to have
• Font:
• - 1 - Rounded is preferred
• - 2 - Colour with reference the logo colours (if possible)
Should not have
• Colour:
• - 1 - To much contrast between colours i.e. balck background with white writing
• - 2 - aggressive colour schemes
• - 3 - Names of Brintavex consultants... These guys are also used by my competetion, only martin is required

```html
<!DOCTYPE html>
<html lang="en">
<head>
<meta charset="utf-8">
<title>Home | Brintavex Group</title>
<link href="https://fonts.googleapis.com/css2?family=Poppins:wght@400;500;600&family=Questrial&display=swap" rel="stylesheet">
<style>
:root{
  --blue:#0d5aa7;
  --blue-deep:#0a4a8c;
  --teal:#1a93c2;
  --ink:#1d1d1f;
  --text:#555a60;
  --grey-btn:#6b6b6b;
  --mist:#eeeeef;
  --footer:#3a3a3c;
  --footer-line:#4b4b4e;
  --white:#ffffff;
}
*{margin:0;padding:0;box-sizing:border-box}
html,body{width:1200px;height:3066px;overflow:hidden}
body{position:relative;background:var(--white);font-family:'Poppins',sans-serif;color:var(--text);font-size:13px;line-height:1.85}
.abs{position:absolute}
h1,h2,h3{font-family:'Questrial',sans-serif;color:var(--ink);font-weight:400;letter-spacing:2px}
h1,h2{-webkit-text-stroke:.6px currentColor}
a{color:inherit;text-decoration:none}
.btn{display:inline-flex;align-items:center;gap:6px;height:42px;padding:0 24px;border-radius:22px;font-size:11px;font-weight:600;color:var(--white);text-transform:uppercase;box-shadow:0 8px 16px rgba(0,0,0,.18)}
.btn-teal{background:var(--teal)}
.btn-grey{background:var(--grey-btn)}
.eyebrow{font-size:11px;font-weight:600;color:var(--blue);letter-spacing:.5px;text-transform:uppercase;line-height:1.4}

/* about background sits behind hero */
.mist{left:0;top:480px;width:1200px;height:1120px;background:linear-gradient(#ffffff 0%,var(--mist) 100%)}

/* header */
.brand{left:88px;top:40px;display:flex;align-items:center;gap:10px;font-weight:600;font-size:18px;color:var(--white);letter-spacing:1px}
.brand .mark{width:38px;height:38px;border-radius:50%;border:3px solid var(--white)}
.nav{right:90px;top:52px;display:flex;gap:30px;align-items:center;font-size:12px;font-weight:500;color:var(--ink)}
.nav .active{color:var(--blue);position:relative}
.nav .active::before{content:"";position:absolute;left:50%;top:-14px;width:18px;height:3px;margin-left:-9px;background:var(--blue)}
.lang{padding:6px 14px;border-radius:6px;box-shadow:0 3px 10px rgba(0,0,0,.12);font-size:10px;background:var(--white)}

.hero-photo{left:-100px;top:-70px;width:650px;height:655px;border-radius:50%;background:linear-gradient(135deg,#6b4a34 0%,#8a6a52 35%,#d9d9d9 60%,#efefef 100%)}
.hero-copy{left:615px;top:216px;width:520px}
.hero-copy h1{font-size:37px;line-height:1.25;letter-spacing:3px}
.hero-copy p{margin:10px 0 20px;font-size:13px}
.slider-dots{left:1142px;top:294px;display:flex;flex-direction:column;gap:10px}
.slider-dots span{width:9px;height:9px;border-radius:50%;border:1.5px solid var(--teal)}
.slider-dots span.on{background:var(--teal)}

/* about */
.about{left:0;top:640px;width:1200px;text-align:center}
.about h2{font-size:29px;margin:2px 0 6px;line-height:1.3}
.about p{width:660px;margin:0 auto 16px;line-height:1.7}
.mouse{left:590px;top:530px}

/* services */
.waves{left:0;top:600px}
.services{left:0;top:1060px;width:1200px;text-align:center;color:#d8e4f2}
.services .eyebrow{color:var(--white)}
.services h2{color:var(--white);font-size:29px;margin:2px 0 8px;line-height:1.3}
.services .intro{width:620px;margin:0 auto;line-height:1.75}
.service{position:absolute;top:1232px;width:300px;text-align:center;color:#d8e4f2}
.service .icon{width:116px;height:116px;border-radius:50%;background:var(--white);margin:0 auto 18px;display:flex;align-items:center;justify-content:center}
.service h3{font-family:'Poppins',sans-serif;font-weight:500;font-size:17px;color:var(--white);letter-spacing:1.5px;margin-bottom:2px}
.service p{font-size:12.5px;line-height:1.6}
.svc-dots{left:0;top:1492px;width:1200px;display:flex;justify-content:center;gap:10px}
.svc-dots span{width:9px;height:9px;border-radius:50%;border:1.5px solid var(--white)}
.svc-dots span.on{background:var(--white)}

/* field reporting */
.field-blob{left:0;top:1688px}
.field{left:615px;top:1730px;width:480px}
.field h2{font-size:29px;line-height:1.3;letter-spacing:3px}
.field .lead{margin:14px 0 16px}
.field ul{list-style:none;margin-bottom:26px}
.field li{position:relative;padding-left:22px;margin-bottom:14px;line-height:1.85}
.field li::before{content:"";position:absolute;left:0;top:7px;width:8px;height:8px;border-radius:50%;border:1.5px solid var(--teal)}

/* connect */
.world{left:10px;top:2360px;width:520px;height:230px;border-radius:40%;background:radial-gradient(ellipse at center,rgba(200,204,210,.35),rgba(255,255,255,0) 70%)}
.connect{left:88px;top:2270px;width:470px}
.connect h2{font-size:29px;line-height:1.45;letter-spacing:3px;margin-bottom:18px}
.connect p{font-size:12.5px;margin-bottom:10px}
.connect .actions{display:flex;gap:14px;margin-top:22px}
.map{left:601px;top:2214px;width:509px;height:361px;border-radius:14px;background:linear-gradient(135deg,#ece8df,#e3e6d8 50%,#e9e4d6);box-shadow:0 6px 20px rgba(0,0,0,.08)}

/* footer */
.footer{left:0;top:2678px;width:1200px;height:388px;background:var(--footer);color:#c6c6c8;font-size:12px}
.foot-brand{left:88px;top:80px;display:flex;align-items:center;gap:12px;font-weight:600;font-size:20px;color:var(--white);letter-spacing:1px}
.foot-brand .mark{width:56px;height:56px;border-radius:50%;border:3px solid var(--white)}
.foot-col{top:78px}
.foot-col h4{font-family:'Questrial',sans-serif;font-weight:400;color:var(--teal);font-size:14px;letter-spacing:2px;margin-bottom:12px}
.foot-col li{list-style:none;line-height:2}
.foot-col li::before{content:"› ";color:#888}
.sub-input{display:flex;align-items:center;width:224px;height:40px;border-radius:20px;background:#2f2f31;color:#8a8a8d;font-size:11px;padding:0 18px;margin:14px 0 14px}
.contact-row{display:flex;gap:10px;margin-bottom:8px;line-height:1.6}
.contact-row svg{flex:none;margin-top:3px}
.socials{display:flex;gap:10px;margin-top:12px}
.socials a{width:30px;height:30px;border-radius:50%;background:#2c4c86}
.foot-rule{left:88px;top:327px;width:1024px;height:1px;background:var(--footer-line)}
.foot-bottom{left:88px;top:348px;width:1024px;display:flex;justify-content:space-between;font-size:11px;color:var(--white)}
.to-top{left:1131px;top:308px;width:36px;height:36px;border-radius:50%;background:var(--teal);display:flex;align-items:center;justify-content:center}
</style>
</head>
<body>

<div class="abs mist"></div>

<!-- hero -->
<div class="abs hero-photo" role="img" aria-label="Desk with a laptop and a white chair, seen from above"></div>
<a class="abs brand" href="#"><span class="mark"></span>BRINTAVEX</a>
<nav class="abs nav">
  <a class="active" href="#">Home</a>
  <a href="#">Our Story</a>
  <a href="#">Services</a>
  <a href="#">Contact</a>
  <span class="lang">EN ▾</span>
</nav>
<section class="abs hero-copy">
  <h1>Project Delivery.<br>Done Differently.</h1>
  <p>We are working with Victoria's most respected delivery partners<br>to deliver unique projects state-wide.</p>
  <a class="btn btn-teal" href="#">Find more →</a>
</section>
<div class="abs slider-dots"><span></span><span class="on"></span><span></span></div>

<!-- about -->
<svg class="abs mouse" width="20" height="34" viewBox="0 0 20 34"><rect x="2" y="2" width="16" height="30" rx="8" fill="none" stroke="#1d1d1f" stroke-width="2"/><line x1="10" y1="8" x2="10" y2="14" stroke="#1d1d1f" stroke-width="2"/></svg>
<section class="abs about">
  <div class="eyebrow">About us</div>
  <h2>Our Story</h2>
  <p>We are an innovative telecommunications services company. We believe technology can truly change peoples' lives, so we are working with Victoria's most respected delivery partners to complete unique projects state-wide.</p>
  <a class="btn btn-grey" href="#">Read more →</a>
</section>

<!-- services -->
<svg class="abs waves" width="1200" height="990" viewBox="0 600 1200 990">
  <path d="M0 1075 C150 1010 300 880 470 905 C620 930 760 1010 900 935 C1050 855 1150 790 1200 640 L1200 1590 L0 1590 Z" fill="var(--blue)"/>
  <path d="M0 1590 L0 1300 C300 1240 700 1420 1200 1280 L1200 1590 Z" fill="var(--blue-deep)" opacity=".35"/>
</svg>
<section class="abs services">
  <div class="eyebrow">What we do</div>
  <h2>Our Services</h2>
  <p class="intro">Working with Brintavex Group enables a single point of contact for your entire project. We have a wide range of specialties and in-house capabilities that allows us to take on full responsibility for projects.</p>
</section>
<div class="service" style="left:110px">
  <div class="icon"><svg width="54" height="54" viewBox="0 0 54 54" fill="none" stroke="#4a5058" stroke-width="2.2"><rect x="12" y="8" width="30" height="38" rx="3"/><path d="M20 8v-3h14v3" stroke="#1a93c2"/><path d="M19 27l6 6 10-12" stroke="#1a93c2"/></svg></div>
  <h3>Project Management</h3>
  <p>Vivamus elementum semper nisi. Aenean vulputate eleifend tellus. Aenean leo ligula, porttitor eu, consequat</p>
</div>
<div class="service" style="left:451px">
  <div class="icon"><svg width="54" height="54" viewBox="0 0 54 54" fill="none" stroke="#4a5058" stroke-width="2.2"><path d="M27 6l17 7v12c0 11-8 19-17 23C18 44 10 36 10 25V13z"/><path d="M20 27l5 5 10-10" stroke="#1a93c2"/></svg></div>
  <h3>Asbestos removal</h3>
  <p>Vivamus elementum semper nisi. Aenean vulputate eleifend tellus. Aenean leo ligula, porttitor eu, consequat</p>
</div>
<div class="service" style="left:792px">
  <div class="icon"><svg width="54" height="54" viewBox="0 0 54 54" fill="none" stroke="#4a5058" stroke-width="2.2"><path d="M10 44V26a17 17 0 0 1 34 0v18"/><path d="M16 44V27a11 11 0 0 1 22 0v17"/><path d="M22 10l-3-5M27 8V3M32 10l3-5" stroke="#1a93c2"/></svg></div>
  <h3>Cable hauling</h3>
  <p>Vivamus elementum semper nisi. Aenean vulputate eleifend tellus. Aenean leo ligula, porttitor eu, consequat</p>
</div>
<div class="abs svc-dots"><span class="on"></span><span></span><span></span></div>

<!-- field reporting -->
<svg class="abs field-blob" width="510" height="440" viewBox="0 0 510 440">
  <path d="M0 40 C120 10 280 -10 420 20 C500 40 505 120 470 210 C430 310 440 400 340 430 C230 460 110 420 0 380 Z" fill="var(--teal)" opacity=".85"/>
  <path role="img" aria-label="Handheld network test instrument in a server rack" d="M0 70 C110 40 250 30 360 60 C440 85 450 160 420 240 C395 310 400 380 300 405 C200 430 90 400 0 360 Z" fill="#3a3f5c"/>
</svg>
<section class="abs field">
  <h2>Field reporting.<br>Simplified.</h2>
  <p class="lead">We've been tirelessly to create an easy to use reporting system.</p>
  <ul>
    <li>We have worked with Formlynx to create simple forms that capture field data in an easy to use app. Reports are easy to obtain and can be downloaded in many popular formats.</li>
    <li>Completed forms are sent from the app to our online server for storage. No need for usbsticks or scanning, simplifying reporting.</li>
  </ul>
  <a class="btn btn-grey" href="#">Read more →</a>
</section>

<!-- connect -->
<div class="abs world" role="img" aria-label="Faint dotted world map"></div>
<section class="abs connect">
  <h2>Connect with Brintavex<br>Group</h2>
  <p>Brintavex Group understands business and we take pride in helping Victorian businesses meet their goals.</p>
  <p>Let Brintavex Group be part of your business's journey, call us today.</p>
  <div class="actions">
    <a class="btn btn-grey" href="tel:+61400555017">+61 400 555 017 →</a>
    <a class="btn btn-teal" href="mailto:info@brintavexgroup.com.au">Email us →</a>
  </div>
</section>
<div class="abs map" role="img" aria-label="Street map of eastern suburbs with office location pin"></div>

<!-- footer -->
<footer class="abs footer">
  <a class="abs foot-brand" href="#"><span class="mark"></span>BRINTAVEX</a>
  <div class="abs foot-col" style="left:331px">
    <h4>Useful Links</h4>
    <ul><li>Home</li><li>Our Story</li><li>Services</li><li>Contact</li><li>Privacy Policy</li></ul>
  </div>
  <div class="abs foot-col" style="left:564px">
    <h4>Newsletter</h4>
    <div>Subscribe to our newsletter</div>
    <div class="sub-input">✉&nbsp; Enter email address</div>
    <a class="btn btn-teal" href="#">Subscribe →</a>
  </div>
  <div class="abs foot-col" style="left:854px;width:260px">
    <h4>Contact us</h4>
    <div class="contact-row"><svg width="10" height="14" viewBox="0 0 10 14"><path d="M5 0a5 5 0 0 1 5 5c0 4-5 9-5 9S0 9 0 5a5 5 0 0 1 5-5z" fill="#1a93c2"/></svg><span>Some Address Line goes<br>here, City, Country.</span></div>
    <div class="contact-row"><svg width="12" height="10" viewBox="0 0 12 10"><rect width="12" height="10" rx="1" fill="#1a93c2"/></svg><a href="mailto:info@brintavexgroup.com.au">info@brintavexgroup.com.au</a></div>
    <div class="contact-row"><svg width="11" height="11" viewBox="0 0 12 12"><path d="M2 0l3 3-1.5 2a7 7 0 0 0 3.5 3.5L9 7l3 3-2 2C5 12 0 7 0 2z" fill="#1a93c2"/></svg><a href="tel:+61400555017">+61 400 555 017</a></div>
    <div class="socials"><a href="#" aria-label="Social profile one"></a><a href="#" aria-label="Social profile two"></a></div>
  </div>
  <div class="abs foot-rule"></div>
  <div class="abs foot-bottom"><span>© 2018, All Rights reserved.</span><span>Terms &amp; Conditions | Site Map</span></div>
  <a class="abs to-top" href="#"><svg width="12" height="8" viewBox="0 0 12 8"><path d="M1 7l5-5 5 5" fill="none" stroke="#fff" stroke-width="2"/></svg></a>
</footer>

</body>
</html>
```